Freelancer working in Gambling Industry

I am a freelancer working in the gambling industry. I used to play poker professionally, so I was thinking having a business card that would have a Jack or Queen or King picture with a twist that is memorable. Feel free to be creative and gutsy. Gonna have name, phone number, skype contact and email as contact details. No existing logo for my company, and no need to name my company either in the business card.

Industry/Entity Type

Gambling

Colors

Designer to choose colors to be used in the design.

```html
<!DOCTYPE html>
<html lang="en">
<head>
<meta charset="utf-8">
<title>Playing Card Business Cards – Design A and Design B</title>
<link href="https://fonts.googleapis.com/css2?family=Courier+Prime:wght@400;700&family=Roboto+Condensed:wght@300;400&display=swap" rel="stylesheet">
<style>
  :root {
    --backdrop: #4b4b4d;
    --card-white: #ffffff;
    --ink: #111111;
    --card-red: #e41e26;
    --card-black: #050505;
    --gold: #c9a514;
    --label: #f2f2f2;
    --icon-grey: #555555;
  }
  * { box-sizing: border-box; margin: 0; padding: 0; }
  html, body { width: 1200px; height: 1200px; overflow: hidden; }
  body { background: var(--backdrop); font-family: "Roboto Condensed", sans-serif; }

  .design-row { position: relative; width: 1200px; height: 600px; }
  .design-label {
    position: absolute; left: 30px; top: 26px;
    font-family: "Roboto Condensed", sans-serif; font-weight: 300;
    font-size: 26px; color: var(--label);
  }

  .card {
    position: absolute; top: 114px; width: 225px; height: 372px;
    border-radius: 12px; overflow: hidden;
  }
  .card--front { left: 355px; background: var(--card-white); }
  .card--back { left: 620px; }

  .card-index {
    position: absolute; font-family: "Courier Prime", monospace; font-weight: 700;
    font-size: 40px; line-height: 1; color: var(--ink);
  }
  .card-index--top { left: 12px; top: 14px; }
  .card-index--bottom { right: 12px; bottom: 14px; }
  .design-row--b .card-index { color: var(--card-red); }

  .contact-block { position: absolute; left: 0; right: 0; top: 140px; text-align: center; color: var(--ink); }
  .contact-name { font-family: "Courier Prime", monospace; font-weight: 400; font-size: 19px; letter-spacing: 0.5px; line-height: 1.2; }
  .contact-phone { font-size: 15px; font-weight: 300; margin-top: 2px; }
  .contact-lines { margin-top: 14px; display: inline-block; text-align: left; font-size: 12px; font-weight: 400; }
  .contact-line { display: flex; align-items: center; gap: 5px; height: 17px; }
  .contact-line svg { flex: none; }

  .card-back-art { position: absolute; inset: 0; width: 100%; height: 100%; }
</style>
</head>
<body>

<section class="design-row design-row--a">
  <h2 class="design-label">Design A</h2>

  <article class="card card--front">
    <span class="card-index card-index--top">K</span>
    <div class="contact-block">
      <p class="contact-name">YOUR NAME</p>
      <p class="contact-phone">555 014 272</p>
      <div class="contact-lines">
        <p class="contact-line">
          <svg width="12" height="9" viewBox="0 0 12 9" aria-hidden="true"><rect x="0.5" y="0.5" width="11" height="8" fill="var(--icon-grey)" stroke="var(--icon-grey)"/><path d="M0.5 0.5 L6 5 L11.5 0.5" fill="none" stroke="#fff" stroke-width="1"/></svg>
          mail@sample.net
        </p>
        <p class="contact-line">
          <svg width="12" height="12" viewBox="0 0 12 12" aria-hidden="true"><circle cx="6" cy="6" r="6" fill="var(--icon-grey)"/></svg>
          chat@sample.net
        </p>
      </div>
    </div>
    <span class="card-index card-index--bottom">K</span>
  </article>

  <article class="card card--back">
    <svg class="card-back-art" viewBox="0 0 225 372">
      <rect width="225" height="372" fill="var(--card-white)"/>
      <rect x="12" y="12" width="201" height="348" rx="5" fill="var(--card-red)" role="img" aria-label="Red ornamental filigree pattern of scrolls and fleurs-de-lis"/>
      <rect x="15" y="15" width="195" height="342" rx="3" fill="none" stroke="var(--card-white)" stroke-width="1.5"/>
    </svg>
  </article>
</section>

<section class="design-row design-row--b">
  <h2 class="design-label">Design B</h2>

  <article class="card card--front">
    <span class="card-index card-index--top">K</span>
    <div class="contact-block">
      <p class="contact-name">YOUR NAME</p>
      <p class="contact-phone">555 014 272</p>
      <div class="contact-lines">
        <p class="contact-line">
          <svg width="12" height="9" viewBox="0 0 12 9" aria-hidden="true"><rect x="0.5" y="0.5" width="11" height="8" fill="var(--icon-grey)" stroke="var(--icon-grey)"/><path d="M0.5 0.5 L6 5 L11.5 0.5" fill="none" stroke="#fff" stroke-width="1"/></svg>
          mail@sample.net
        </p>
        <p class="contact-line">
          <svg width="12" height="12" viewBox="0 0 12 12" aria-hidden="true"><circle cx="6" cy="6" r="6" fill="var(--icon-grey)"/></svg>
          chat@sample.net
        </p>
      </div>
    </div>
    <span class="card-index card-index--bottom">K</span>
  </article>

  <article class="card card--back">
    <svg class="card-back-art" viewBox="0 0 225 372">
      <defs>
        <radialGradient id="suit-lattice-tone" cx="50%" cy="50%" r="70%">
          <stop offset="0" stop-color="#1d1806"/>
          <stop offset="1" stop-color="#050505"/>
        </radialGradient>
      </defs>
      <rect width="225" height="372" fill="var(--card-black)"/>
      <rect x="8" y="8" width="209" height="356" rx="9" fill="none" stroke="var(--gold)" stroke-width="3"/>
      <rect x="13" y="13" width="199" height="346" rx="6" fill="url(#suit-lattice-tone)" role="img" aria-label="Gold lattice pattern of card suit symbols on black"/>
      <rect x="13" y="13" width="199" height="346" rx="6" fill="none" stroke="var(--gold)" stroke-width="1"/>
    </svg>
  </article>
</section>

</body>
</html>
```